Jolly Snaps - Photobooth hire

Photobooth flyer

We have just got our new photobooth and are ready to get the marketing side of things done! Our flyer needs to attract weddings, birthdays, corporate events, hens nights ect. For the winning flyer I would also like to follow up with the designer and get started with logo, business cards, web designs, car stickers etc. The flyer needs include this information

prices. $450 - 3 hrs $550 - 4 hrs $650 - 5 hrs. For extra time, additional payment can be made on the night. Our booths are also built with the flexibility to break down into smaller booths suitable for children. Prices start from $250 for kids parties and day time events.

All packages include
Unlimited prints
2 photo strips, one for you and one for friend.
Choice of different filters
Green screen technology - optional
Photobooth attendant
Use of cheeky props.

Call us for information and prices on additional items like photo albums, magnets, personalized photo strips, and more :)
0461927584

Feel free to change wording and add some character ;P

I would also like there to be sort of like a photostrip wave that I can add our photos. We will have them in a week :)
Thankyou for your time, am really looking forward to seeing what you come up with!!

Marketing

Sans Serif

8869ae

• I have uploaded a couple of flyers that I have come across and really like.. I like how the background is grey with some bold colour coming through.
• It also makes it hard because I don't have a logo.. But even in the heading, photobooth, I was thinking maybe a moustache underneath booth. Or even a cute little camera in one of the O's.

```html
<!DOCTYPE html>
<html lang="en">
<head>
<meta charset="utf-8">
<title>Jolly Snaps – Photobooth Hire Flyer</title>
<link rel="stylesheet" href="https://fonts.googleapis.com/css2?family=Ubuntu:wght@300;400;500&display=swap">
<style>
  :root {
    --backdrop: #e4e4e4;
    --paper: #ffffff;
    --coral: #ee7468;
    --slate: #4f5d7a;
    --ink: #3a3a3a;
    --rule: #e6c9c5;
    --photo-a: #5b6675;
    --photo-b: #c9b8a8;
    --photo-c: #d9dde3;
  }
  * { box-sizing: border-box; margin: 0; padding: 0; }
  html, body { width: 1200px; height: 987px; overflow: hidden; }
  body {
    background: var(--backdrop);
    font-family: "Ubuntu", sans-serif;
    color: var(--ink);
    display: flex; align-items: center; justify-content: center;
  }
  .flyer {
    position: relative;
    width: 672px; height: 950px;
    background: var(--paper);
    box-shadow: 0 8px 30px rgba(0,0,0,.15);
    overflow: hidden;
  }
  .swoosh { position: absolute; inset: 0; z-index: 0; }
  .flyer > *:not(.swoosh) { z-index: 1; }
  .brand {
    position: absolute; left: 56px; top: 48px;
    font-size: 64px; font-weight: 400; color: var(--coral);
    letter-spacing: 1px;
  }
  .collage { position: absolute; left: 70px; top: 150px; width: 420px; height: 260px; }
  .collage .frame {
    position: absolute; background: var(--paper); padding: 7px;
    box-shadow: 0 2px 6px rgba(0,0,0,.25);
  }
  .collage .frame span { display: block; width: 100%; height: 100%; background: linear-gradient(135deg, var(--photo-a), var(--photo-b) 60%, var(--photo-c)); }
  .price-badge {
    position: absolute; left: 478px; top: 250px;
    width: 120px; height: 120px; border-radius: 50%;
    background: var(--coral); color: #fff; text-align: center;
    display: flex; flex-direction: column; justify-content: center;
    box-shadow: 0 0 0 4px rgba(238,116,104,.25);
  }
  .price-badge small { font-size: 10px; font-weight: 300; line-height: 1.3; }
  .price-badge strong { font-size: 30px; font-weight: 400; line-height: 1.1; }
  .headline {
    position: absolute; left: 56px; top: 452px; width: 560px;
    font-size: 27px; font-weight: 300; color: var(--coral);
    border-bottom: 1px solid var(--rule); padding-bottom: 10px;
  }
  .headline .accent { color: var(--slate); }
  .headline .star { font-size: 16px; vertical-align: middle; }
  .thumbs { position: absolute; left: 56px; top: 512px; width: 560px; display: flex; justify-content: space-between; }
  .thumbs .thumb { display: flex; flex-direction: column; align-items: center; gap: 6px; }
  .thumbs .thumb span {
    display: block; width: 70px; height: 54px; border: 4px solid var(--paper);
    box-shadow: 0 1px 4px rgba(0,0,0,.3);
    background: linear-gradient(135deg, var(--photo-a), var(--photo-b));
  }
  .thumbs .thumb i { width: 5px; height: 5px; border-radius: 50%; background: var(--coral); }
  .details { position: absolute; left: 56px; top: 610px; width: 340px; font-size: 15px; line-height: 1.45; }
  .rates { font-size: 16px; margin-bottom: 8px; }
  .rates .sep { color: var(--coral); }
  .rates .kids { color: var(--coral); }
  .note { font-size: 13px; margin-bottom: 8px; }
  .inclusions { list-style: none; }
  .inclusions .accent { color: var(--coral); }
  .contact { position: absolute; left: 420px; top: 610px; width: 200px; border-left: 1px solid var(--rule); padding-left: 18px; }
  .contact p { font-size: 12px; line-height: 1.5; }
  .contact .phone { font-size: 34px; color: var(--coral); margin-top: 16px; letter-spacing: .5px; }
</style>
</head>
<body>
  <main class="flyer">
    <svg class="swoosh" viewBox="0 0 672 950" aria-hidden="true">
      <path d="M525 110 C 570 230, 430 330, 230 385 C 130 410, 50 425, 0 445 L 0 405 C 60 390, 150 370, 240 345 C 420 295, 560 225, 525 110 Z" fill="var(--coral)"/>
    </svg>

    <h1 class="brand">Jolly Snaps</h1>

    <div class="collage" role="img" aria-label="Collage of tilted event photos from photobooth sessions">
      <div class="frame" style="left:0;top:70px;width:130px;height:100px;transform:rotate(-8deg)"><span></span></div>
      <div class="frame" style="left:110px;top:110px;width:120px;height:110px;transform:rotate(6deg)"><span></span></div>
      <div class="frame" style="left:200px;top:0;width:150px;height:110px;transform:rotate(-5deg)"><span></span></div>
      <div class="frame" style="left:220px;top:120px;width:140px;height:120px;transform:rotate(-10deg)"><span></span></div>
      <div class="frame" style="left:330px;top:90px;width:90px;height:90px;transform:rotate(8deg)"><span></span></div>
      <div class="frame" style="left:130px;top:20px;width:90px;height:80px;transform:rotate(12deg)"><span></span></div>
    </div>

    <div class="price-badge">
      <small>Prices Start from</small>
      <strong>$250</strong>
      <small>for kids parties<br>&amp; daytime</small>
    </div>

    <h2 class="headline"><span class="star">★</span> Professional <span class="accent">Photography Booth</span> <span class="star">★</span></h2>

    <div class="thumbs" role="img" aria-label="Row of small photobooth snapshots">
      <div class="thumb"><span></span><i></i></div>
      <div class="thumb"><span></span><i></i></div>
      <div class="thumb"><span></span><i></i></div>
      <div class="thumb"><span></span><i></i></div>
      <div class="thumb"><span></span><i></i></div>
      <div class="thumb"><span></span><i></i></div>
    </div>

    <section class="details">
      <p class="rates">$450 - 3hrs <span class="sep">★</span> $550 - 4hrs <span class="sep">★</span> $650 - 5hrs <span class="sep">★</span> <span class="kids">$250 for kids parties &amp; daytime events</span></p>
      <p class="note">For extra time, additional payment can be made on the night. Our booths are also built with the flexibility to break down into smaller booths suitable for children.</p>
      <ul class="inclusions">
        <li class="accent">All packages include</li>
        <li>Unlimited prints</li>
        <li class="accent">2 photo strips, one for you and one for friend.</li>
        <li>Choice of different filters</li>
        <li class="accent">Green screen technology - optional</li>
        <li>Photobooth attendant</li>
        <li class="accent">Use of cheeky props.</li>
      </ul>
    </section>

    <aside class="contact">
      <p>Call us for information and prices on additional items like photo albums, magnets, personalized photo strips, and more :)</p>
      <p class="phone">0461927584</p>
    </aside>
  </main>
</body>
</html>
```